Building company needs a new logo and letterhead design

We need a new and refreshed logo and letterhead design for an existing building company. We specialise in residential as well as commercial building/construction, design and project management. Our company name is Talvek Constructions Pty Ltd. Our primary colours that we want to use are black/orange/white. We do renovations/alterations/new homes both residential and commercial. We are a medium sized building company. We want something simple and modern.

Industry/Entity Type

Residential

```html
<!DOCTYPE html>
<html lang="en">
<head>
<meta charset="utf-8">
<title>Talvek Constructions Pty Ltd – Letterhead</title>
<link rel="stylesheet" href="https://fonts.googleapis.com/css2?family=Crimson+Pro:wght@400;700&display=swap">
<style>
  :root {
    --paper: #ffffff;
    --brand-orange: #f07a1a;
    --ink: #111111;
    --label-brown: #5a2a0c;
    --wave-light: rgba(246, 201, 164, 0.55);
    --wave-mid: rgba(217, 138, 78, 0.35);
    --wave-fade: rgba(255, 255, 255, 0);
  }
  * { margin: 0; padding: 0; box-sizing: border-box; }
  html, body { width: 869px; height: 1200px; overflow: hidden; background: var(--paper); }
  .letterhead {
    position: relative;
    width: 869px;
    height: 1200px;
    background: var(--paper);
    font-family: "Crimson Pro", "Palatino Linotype", Georgia, serif;
    color: var(--ink);
    overflow: hidden;
  }

  .footer-wave {
    position: absolute;
    left: 0;
    right: 0;
    bottom: 0;
    height: 340px;
    background:
      radial-gradient(ellipse 75% 45% at 70% 100%, var(--wave-mid), var(--wave-fade) 70%),
      linear-gradient(to bottom, var(--wave-fade) 0%, var(--wave-light) 100%);
  }

  .brand { position: absolute; left: 29px; top: 37px; display: flex; align-items: flex-start; }
  .brand-square { width: 86px; height: 86px; background: var(--ink); flex: none; }
  .brand-name { margin-left: 16px; font-weight: 400; line-height: 1; }
  .brand-name .primary {
    display: block;
    font-size: 54px;
    margin-top: 12px;
    letter-spacing: 0.5px;
    color: var(--brand-orange);
  }
  .brand-name .secondary {
    display: block;
    font-size: 17px;
    margin-top: 0;
    color: var(--ink);
  }

  .contact {
    position: absolute;
    right: 27px;
    top: 957px;
    text-align: right;
    font-style: normal;
    font-size: 21.5px;
    line-height: 24px;
  }
  .contact .label { color: var(--label-brown); font-weight: 700; }
  .contact-group + .contact-group { margin-top: 16px; }
  .contact-group.online { margin-top: 11px; }
</style>
</head>
<body>
<div class="letterhead">
  <div class="footer-wave" role="img" aria-label="Soft flowing peach and bronze wave graphic across the foot of the page"></div>

  <header class="brand">
    <div class="brand-square"></div>
    <div class="brand-name">
      <span class="primary">Talvek</span>
      <span class="secondary">Constructions Pty Ltd</span>
    </div>
  </header>

  <address class="contact">
    <div class="contact-group">
      <div><span class="label">Address:</span> PO Box 312</div>
      <div>Ashbury</div>
      <div>NSW&nbsp;&nbsp;2193</div>
    </div>
    <div class="contact-group">
      <div><span class="label">Tel:</span> 0295550148</div>
      <div><span class="label">Fax:</span> 0295550162</div>
      <div><span class="label">Mobile:</span> 0412550937</div>
    </div>
    <div class="contact-group online">
      <div><span class="label">Email:</span> office@talvekmail.com</div>
      <div><span class="label">Web:</span> www.talvekconstructions.com.au</div>
    </div>
  </address>
</div>
</body>
</html>
```